Smart, intuitive SaaS software dashboard design

PactBloom is an innovative modern SaaS (software as a service) solution for contract and meeting management.

What we are looking for is fresh ideas for our dashboard. We do not need web coding or actionable wireframes now – but purely great design ideas from where to continue forward.

How should a modern web software dashboard look like? Fresh, intuitive, easy-to-use, and adaptable for responsive mobile designs. We hope that when the user logs into the service and sees the dashboard, he/she gets a good big picture of the current status of the most important documents of his/hers company.

To get to know the service and see the components, we kindly ask you to register to our service at www.pactbloom-demo.net and to utilize the free trial (30 days) so you can see the existing dashboard live. And also try out how it works. Might help you to get ideas how to improve it.

(The designer we will choose might be offered later on to design some other pages as well (contract view and edit pages, meeting page etc).)

You’ll find additional information in the attachment.

You’ll find more information of the company and the service also at www.pactbloom-demo.net

Target Market(s)

Global

Industry/Entity Type

Business Management

Number of Pages Required

1 page

Font styles to use
Sans Serif

Requirements
Must have
• 1) Clear design idea for us to iterate from, 2) Modern look and feel - elegant & bold at the same time - still with credibility in our target group. And 3) Suitable for dashboard usage - it should it a clear big picture for the user.
• UPDATE:
• Users should see most important things with one glance. Therefore we would like to see AT LEAST these items mentioned below on the first page.
• NOTE: if all these things are visible on the dashboard, the menu list is maybe not needed on the left. (And there might be some icons on the top header with needed settings/inbox features anyway.)
• NOTE2: as explained earlier, the design should be responsive i.e. work without modifications in PC, iPad and mobile (the areas/boxes would just rearrange themselves on top of each other.)
• -First area should be Documents, which would include different document categories: Contracts, Finance & Admin and HR
• -All different types of Meetings could be the next area (upcoming ones clearly visible with date and maybe description, time and location visible also).
• -Reminders and Activity Feed (they might also be together in top of each other, so that Reminder is visible first and Activity feed can be chosen from the tab.)
• -Virtual Datarooms (maybe 1-3 different ones with some analytics for each visible e.g. like usage/visits per day)
• Saved searches in very important list as users can save their most important searches. There are typically many of these, so at least 5 should be visible and then see all button (maybe even more could be visible if they fit on your design)
• My Latest is also important.
• (As explained, Action Required area is NOT needed anymore).
Nice to have
• Surprise us!
Should not have
• Please avoid the boring traditional legacy stuff and the common report dashboards.
• You do not need design a 100% mockup for the techie to continue with. The ideas count.

```html
<!DOCTYPE html>
<html lang="en">
<head>
<meta charset="utf-8">
<title>PactBloom Dashboard</title>
<link href="https://fonts.googleapis.com/css2?family=Lato:wght@300;400;700&display=swap" rel="stylesheet">
<style>
:root{
  --sidebar-top:#2f8cf0;
  --sidebar-bottom:#3bbcf6;
  --sidebar-active:rgba(255,255,255,0.14);
  --header-bg:#ffffff;
  --search-bg:#e6eaed;
  --content-bg:#eef1f3;
  --card-bg:#ffffff;
  --accent-blue:#3a9ef0;
  --title-navy:#2f4e7a;
  --text-muted:#9aa6b2;
  --text-light:#c3cbd3;
  --line:#e5e9ed;
  --panel-top:#355f8f;
  --panel-bottom:#3e6173;
  --panel-text:rgba(255,255,255,0.55);
  --high:#4fd6de;
  --mid:#f8d252;
  --low:#d17be6;
  --badge:#1f4a86;
}
*{box-sizing:border-box;margin:0;padding:0}
html,body{width:1200px;height:720px;overflow:hidden;background:var(--content-bg)}
body{font-family:'Lato',sans-serif;position:relative}
.sidebar{position:absolute;left:0;top:0;width:94px;height:720px;background:linear-gradient(180deg,var(--sidebar-top),var(--sidebar-bottom))}
.brand{position:absolute;top:40px;left:0;width:94px;text-align:center;color:#fff;font-weight:700;font-size:14px}
.nav-item{position:absolute;left:0;width:94px;height:93px;display:flex;align-items:center;justify-content:center}
.nav-item.active{background:var(--sidebar-active)}
.chat-button{position:absolute;left:16px;top:628px;width:60px;height:60px;border-radius:50%;background:rgba(255,255,255,0.22);display:flex;align-items:center;justify-content:center}
.chat-badge{position:absolute;left:58px;top:617px;width:23px;height:23px;border-radius:50%;background:var(--badge);color:#fff;font-size:11px;font-weight:700;display:flex;align-items:center;justify-content:center}
.topbar{position:absolute;left:94px;top:0;width:825px;height:94px;background:var(--header-bg)}
.tab{position:absolute;top:32px;font-size:21px;font-weight:300}
.tab.current{left:40px;color:var(--accent-blue)}
.tab.other{left:246px;color:var(--text-light)}
.tab-dot{position:absolute;left:334px;top:35px;width:7px;height:7px;border-radius:50%;background:var(--high)}
.avatar{position:absolute;left:664px;top:23px;width:52px;height:52px;border-radius:50%;background:radial-gradient(circle at 50% 40%,#c9a58e,#6d8fa8)}
.user-name{position:absolute;left:730px;top:40px;font-size:13px;color:#3b4652}
.searchbar{position:absolute;left:94px;top:94px;width:825px;height:94px;background:var(--search-bg)}
.search-icon{position:absolute;left:37px;top:33px}
.search-divider{position:absolute;left:96px;top:23px;width:1px;height:50px;background:#cfd6dc}
.search-placeholder{position:absolute;left:133px;top:33px;font-size:21px;font-weight:300;color:#aab4be}
.filter{position:absolute;left:707px;top:40px;font-size:14px;color:#7d8b99;display:flex;align-items:center;gap:10px}
.card{position:absolute;background:var(--card-bg);border-radius:4px;box-shadow:0 2px 6px rgba(40,70,100,0.05);padding:34px 32px 0 32px}
.card-title{font-size:15px;font-weight:700;color:var(--title-navy);letter-spacing:.1px}
.priority-ring{position:absolute;right:32px;top:35px;width:17px;height:17px;border-radius:50%;border:2.5px solid}
.ring-high{border-color:var(--high)}
.ring-mid{border-color:var(--mid)}
.ring-low{border-color:var(--low)}
.doc-list{list-style:none;margin-top:8px;margin-right:6px}
.doc-list li{display:flex;justify-content:space-between;height:47px;align-items:center;font-size:14px;color:var(--text-muted);border-bottom:1px solid var(--line)}
.doc-list li:last-child{border-bottom:none}
.card-body{margin-top:12px;font-size:14px;line-height:26px;color:#a9b4bf}
.tags{display:flex;flex-wrap:wrap;gap:10px;margin-top:22px;width:290px}
.tag{height:35px;border:1px solid #dfe4e9;border-radius:18px;padding:0 26px;display:flex;align-items:center;font-size:12px;color:#c3cbd3;text-transform:uppercase}
.timestamp{display:flex;align-items:center;gap:10px;margin-top:26px;font-size:14px;font-weight:700;color:var(--text-light)}
.fade{position:absolute;left:94px;top:560px;width:825px;height:160px;background:linear-gradient(180deg,rgba(238,241,243,0),rgba(238,241,243,0.75))}
.reminders{position:absolute;left:919px;top:0;width:281px;height:720px;background:linear-gradient(180deg,var(--panel-top),var(--panel-bottom))}
.panel-label{position:absolute;left:33px;font-size:17px;font-weight:700;color:var(--panel-text)}
.month-nav{position:absolute;left:33px;top:92px;width:215px;display:flex;justify-content:space-between;align-items:center;color:#fff;font-weight:700;font-size:15px}
.month-rule{position:absolute;left:36px;top:141px;width:212px;height:1px;background:rgba(255,255,255,0.12)}
.week-highlight{position:absolute;left:20px;top:243px;width:246px;height:33px;border-radius:17px;background:rgba(255,255,255,0.12)}
.calendar{position:absolute;left:26px;top:172px;display:grid;grid-template-columns:repeat(7,34px);grid-auto-rows:38.8px;font-size:15px;font-weight:700;color:var(--panel-text);text-align:center;align-items:center}
.calendar .current-week{color:#fff}
.priority-list{position:absolute;left:34px;top:492px;list-style:none}
.priority-list li{display:flex;align-items:center;gap:12px;height:29.5px;font-size:15px;font-weight:700;color:var(--panel-text)}
.priority-list .ring{width:16px;height:16px;border-radius:50%;border:2.5px solid}
</style>
</head>
<body>
<nav class="sidebar">
  <div class="brand">PactBloom</div>
  <div class="nav-item" style="top:132px">
    <svg width="38" height="34" viewBox="0 0 38 34" fill="none" stroke="#fff" stroke-width="2.2" opacity=".8"><rect x="2" y="8" width="34" height="24" rx="2"/><path d="M13 8V3h12v5M2 18h34M17 18v4h4v-4"/></svg>
  </div>
  <div class="nav-item active" style="top:226px">
    <svg width="40" height="36" viewBox="0 0 40 36" fill="none" stroke="#fff" stroke-width="2.2" stroke-linejoin="round"><path d="M20 3L38 12 20 21 2 12z"/><path d="M2 18l18 9 18-9M2 24l18 9 18-9"/></svg>
  </div>
  <div class="nav-item" style="top:329px">
    <svg width="38" height="38" viewBox="0 0 38 38" fill="none" stroke="#fff" stroke-width="2.2" opacity=".8"><path d="M2 2v34h34"/><rect x="7" y="14" width="5" height="18"/><rect x="15" y="20" width="5" height="12"/><rect x="23" y="16" width="5" height="16"/></svg>
  </div>
  <div class="nav-item" style="top:415px">
    <svg width="36" height="40" viewBox="0 0 36 40" fill="none" stroke="#fff" stroke-width="2.2" opacity=".8"><path d="M6 2v36M18 2v36M30 2v36M2 24h8M14 12h8M26 28h8"/></svg>
  </div>
  <div class="chat-button">
    <svg width="28" height="26" viewBox="0 0 28 26" fill="none" stroke="#fff" stroke-width="2.4" stroke-linejoin="round"><path d="M6 3h16a4 4 0 0 1 4 4v8a4 4 0 0 1-4 4H13l-6 5v-5H6a4 4 0 0 1-4-4V7a4 4 0 0 1 4-4z"/><circle cx="9" cy="11" r="1" fill="#fff"/><circle cx="14" cy="11" r="1" fill="#fff"/><circle cx="19" cy="11" r="1" fill="#fff"/></svg>
  </div>
  <div class="chat-badge">3</div>
</nav>

<header class="topbar">
  <div class="tab current">Action Required</div>
  <div class="tab other">Meetings</div>
  <span class="tab-dot"></span>
  <div class="avatar" role="img" aria-label="User profile photo"></div>
  <div class="user-name">Marcus</div>
</header>

<div class="searchbar">
  <svg class="search-icon" width="30" height="30" viewBox="0 0 30 30" fill="none" stroke="#3a5f8a" stroke-width="2.2"><circle cx="12" cy="12" r="10"/><path d="M19.5 19.5L28 28"/></svg>
  <span class="search-divider"></span>
  <div class="search-placeholder">Search keywords</div>
  <div class="filter">Contract <svg width="11" height="6" viewBox="0 0 11 6"><path d="M0 0h11L5.5 6z" fill="#7d8b99"/></svg></div>
</div>

<section class="card" style="left:134px;top:226px;width:354px;height:269px">
  <h2 class="card-title">DOCUMENT</h2>
  <span class="priority-ring ring-high"></span>
  <ul class="doc-list">
    <li><span>Contracts</span><span>9</span></li>
    <li><span>Finance</span><span>3</span></li>
    <li><span>Admin</span><span>6</span></li>
    <li><span>HR</span><span>2</span></li>
  </ul>
</section>

<section class="card" style="left:527px;top:226px;width:354px;height:313px">
  <h2 class="card-title">MEETINGS</h2>
  <span class="priority-ring ring-mid"></span>
  <p class="card-body">Lorem ipsum dolor sit amet, consectetur adipisicing elit, sed do eiusmod tempor incidi-dunt ut labore et.</p>
  <div class="tags"><span class="tag">Tag one</span><span class="tag">One more tag</span><span class="tag">Tag three</span></div>
  <div class="timestamp">
    <svg width="20" height="20" viewBox="0 0 20 20" fill="none" stroke="#c3cbd3" stroke-width="2"><circle cx="10" cy="10" r="8.5"/><path d="M10 5v5h4"/></svg>
    5 min ago
  </div>
</section>

<section class="card" style="left:134px;top:523px;width:354px;height:230px">
  <h2 class="card-title">PICTURES IN THE SKY</h2>
  <span class="priority-ring ring-low"></span>
  <p class="card-body">Lorem ipsum dolor sit amet, consectetur adipisicing elit, sed do eiusmod tempor incidi-dunt ut labore et.</p>
  <div class="tags"><span class="tag">Tag one</span><span class="tag">One more tag</span></div>
</section>

<section class="card" style="left:529px;top:567px;width:354px;height:200px">
  <h2 class="card-title">SPACE THE FINAL FRONTIER</h2>
  <span class="priority-ring ring-high"></span>
  <p class="card-body">Lorem ipsum dolor sit amet, consectetur adipisicing elit, sed do eiusmod tempor incidi-dunt ut labore et.</p>
</section>

<div class="fade"></div>

<aside class="reminders">
  <h2 class="panel-label" style="top:47px">REMINDERS</h2>
  <div class="month-nav">
    <svg width="10" height="16" viewBox="0 0 10 16" fill="none" stroke="#fff" stroke-width="2.2"><path d="M8 2L2 8l6 6"/></svg>
    <span>JUNE 2016</span>
    <svg width="10" height="16" viewBox="0 0 10 16" fill="none" stroke="#fff" stroke-width="2.2"><path d="M2 2l6 6-6 6"/></svg>
  </div>
  <span class="month-rule"></span>
  <span class="week-highlight"></span>
  <div class="calendar">
    <span>M</span><span>T</span><span>W</span><span>T</span><span>F</span><span>S</span><span>S</span>
    <span>28</span><span>29</span><span>30</span><span>31</span><span>1</span><span>2</span><span>3</span>
    <span class="current-week">4</span><span class="current-week">5</span><span class="current-week">6</span><span class="current-week">6</span><span class="current-week">7</span><span class="current-week">8</span><span class="current-week">9</span>
    <span>10</span><span>11</span><span>12</span><span>13</span><span>14</span><span>15</span><span>16</span>
    <span>17</span><span>18</span><span>19</span><span>19</span><span>20</span><span>21</span><span>22</span>
    <span>23</span><span>24</span><span>25</span><span>26</span><span>27</span><span>28</span><span>29</span>
  </div>
  <h2 class="panel-label" style="top:450px">PRIORITIES</h2>
  <ul class="priority-list">
    <li><span class="ring" style="border-color:var(--high)"></span>HIGH</li>
    <li><span class="ring" style="border-color:var(--mid)"></span>MID</li>
    <li><span class="ring" style="border-color:var(--low)"></span>LOW</li>
  </ul>
</aside>
</body>
</html>
```